Four in One (Flexible infographic for Content Management Industry)

See attachment.
A graphic depicting 4 products, where each can stand on its own and each can be combined with others, but where, if all are taken together, the best result is achieved (the "super product").
Intended use is web. See attached file as an example.
The most basic idea is as the attached diagram shows, where 4 rectangles are arranged in a quadrangle, with a middle rectangle in the center representing the combined 4 products. This concept is fine except it is a bit too obvious as it stands. We are looking for either a variation of this or another concept.
The audience is technical + professional + enterprise - NOT consumers. Hence the design should be conservative in nature.
We are aware of tools like as Canva or Pictogram where such graphics are available, but we are looking for something with a bit more imagination and flexibility.
This graphic should be targeted to web sites and be delivered with vector-based (SVG) graphics.

```html
<!DOCTYPE html>
<html lang="en">
<head>
<meta charset="utf-8">
<title>Super Product – Four in One</title>
<link rel="stylesheet" href="https://fonts.googleapis.com/css2?family=Outfit:wght@400;500;600&display=swap">
<style>
  :root {
    --bg: #2f2a3f;
    --doc-dark: #bf3a12;
    --doc-light: #e5461d;
    --doc-icon: #f2562a;
    --sec-dark: #3e5069;
    --sec-light: #5e77a0;
    --sec-icon: #6f8cba;
    --erp-dark: #503b70;
    --erp-light: #744f9f;
    --erp-icon: #7b58ad;
    --dig-dark: #5a8a48;
    --dig-light: #6eab5a;
    --dig-icon: #6eab5a;
    --gold: #a6761c;
    --text: #ffffff;
    --button-text: #bfeaf5;
    --play: #f0401e;
  }
  * { margin: 0; padding: 0; box-sizing: border-box; }
  html, body { width: 1200px; height: 675px; overflow: hidden; background: var(--bg); }
  body { font-family: "Outfit", sans-serif; color: var(--text); position: relative; }
  .stage { position: absolute; inset: 0; }
  .block { position: absolute; }
  .title {
    font-weight: 600; font-size: 16.5px; line-height: 19px;
    letter-spacing: 0.9px; text-transform: uppercase;
  }
  .title--right { text-align: right; }
  .summary { font-size: 13.2px; line-height: 15px; width: 260px; letter-spacing: 0.1px; }
  .divider { height: 1px; width: 252px; margin: 8px 0 10px; }
  .divider--doc { background: #e0603a; }
  .divider--sec { background: #6c80a0; }
  .divider--erp { background: #7a63a0; }
  .divider--dig { background: #7fae6c; }
  .checks { list-style: none; font-size: 13px; letter-spacing: 0.2px; }
  .checks li { position: relative; padding-left: 21px; height: 24.6px; line-height: 24.6px; }
  .checks li::before {
    content: ""; position: absolute; left: 6px; top: 7px;
    width: 5px; height: 9px; border-right: 2.2px solid var(--text); border-bottom: 2.2px solid var(--text);
    transform: rotate(40deg);
  }
  .learn-more {
    position: absolute; width: 107px; height: 25px;
    border: 1px solid var(--text); border-radius: 13px;
    color: var(--button-text); font-size: 13px; font-weight: 500; letter-spacing: 0.3px;
    line-height: 23px; padding-left: 11px; text-decoration: none;
  }
  .learn-more::after {
    content: ""; position: absolute; right: 4px; top: 2.5px;
    width: 18px; height: 18px; border-radius: 50%; background: var(--play);
  }
  .learn-more::before {
    content: ""; position: absolute; right: 9px; top: 7.5px; z-index: 1;
    border-left: 6px solid #fff; border-top: 4px solid transparent; border-bottom: 4px solid transparent;
  }
  .hub-label {
    position: absolute; left: 534px; top: 314px; width: 132px; text-align: center;
    font-weight: 600; font-size: 19px; line-height: 23px; letter-spacing: 1px;
  }
</style>
</head>
<body>
<svg class="stage" width="1200" height="675" viewBox="0 0 1200 675" aria-hidden="true">
  <defs>
    <clipPath id="clip-doc"><path d="M85,75 H563 A28,28 0 0 1 591,103 V331 H141 A56,56 0 0 1 85,275 Z"/></clipPath>
    <clipPath id="clip-sec"><path d="M637,75 H1115 V275 A56,56 0 0 1 1059,331 H609 V103 A28,28 0 0 1 637,75 Z"/></clipPath>
    <clipPath id="clip-erp"><path d="M141,345 H591 V572 A28,28 0 0 1 563,600 H85 V401 A56,56 0 0 1 141,345 Z"/></clipPath>
    <clipPath id="clip-dig"><path d="M609,345 H1059 A56,56 0 0 1 1115,401 V600 H637 A28,28 0 0 1 609,572 Z"/></clipPath>
  </defs>

  <g class="card card--doc" clip-path="url(#clip-doc)">
    <rect x="85" y="75" width="314" height="256" fill="var(--doc-dark)"/>
    <rect x="399" y="75" width="192" height="256" fill="var(--doc-light)"/>
    <circle cx="600" cy="338" r="172" fill="var(--doc-dark)"/>
  </g>
  <g class="card card--sec" clip-path="url(#clip-sec)">
    <rect x="609" y="75" width="192" height="256" fill="var(--sec-light)"/>
    <rect x="801" y="75" width="314" height="256" fill="var(--sec-dark)"/>
    <circle cx="600" cy="338" r="172" fill="var(--sec-dark)"/>
  </g>
  <g class="card card--erp" clip-path="url(#clip-erp)">
    <rect x="85" y="345" width="314" height="255" fill="var(--erp-dark)"/>
    <rect x="399" y="345" width="192" height="255" fill="var(--erp-light)"/>
    <circle cx="600" cy="338" r="172" fill="var(--erp-dark)"/>
  </g>
  <g class="card card--dig" clip-path="url(#clip-dig)">
    <rect x="609" y="345" width="192" height="255" fill="var(--dig-light)"/>
    <rect x="801" y="345" width="314" height="255" fill="var(--dig-dark)"/>
    <circle cx="600" cy="338" r="172" fill="var(--dig-dark)"/>
  </g>

  <g class="dividers" stroke="#ffffff" stroke-width="1.2" stroke-dasharray="6 5">
    <line x1="399" y1="75" x2="399" y2="331"/>
    <line x1="801" y1="75" x2="801" y2="331"/>
    <line x1="399" y1="345" x2="399" y2="600"/>
    <line x1="801" y1="345" x2="801" y2="600"/>
  </g>

  <!-- server rack icon -->
  <g class="icon icon--server" fill="var(--doc-icon)" transform="translate(512 251) rotate(45)">
    <rect x="-36" y="-13" width="20" height="58" rx="3"/>
    <rect x="-10" y="-30" width="20" height="58" rx="3"/>
    <rect x="16" y="-45" width="20" height="58" rx="3"/>
    <g fill="var(--doc-dark)">
      <circle cx="-26" cy="37" r="2.6"/><circle cx="0" cy="20" r="2.6"/><circle cx="26" cy="5" r="2.6"/>
      <rect x="-31" y="-7" width="10" height="1.6"/><rect x="-31" y="-3" width="10" height="1.6"/>
      <rect x="-5" y="-24" width="10" height="1.6"/><rect x="-5" y="-20" width="10" height="1.6"/>
      <rect x="21" y="-39" width="10" height="1.6"/><rect x="21" y="-35" width="10" height="1.6"/>
    </g>
  </g>

  <!-- document with shield icon -->
  <g class="icon icon--secure-doc" transform="translate(683 251) rotate(45)">
    <rect x="-20" y="-32" width="40" height="56" rx="2" fill="var(--sec-icon)"/>
    <g stroke="var(--sec-dark)" stroke-width="1.8">
      <line x1="-10" y1="-18" x2="10" y2="-18"/><line x1="-10" y1="-12" x2="10" y2="-12"/><line x1="-10" y1="-6" x2="4" y2="-6"/>
    </g>
    <path d="M-4,18 L10,12 L24,18 V28 C24,36 16,40 10,42 C4,40 -4,36 -4,28 Z" fill="var(--sec-icon)" stroke="var(--sec-dark)" stroke-width="2"/>
    <path d="M5,27 L9,31 L16,23" fill="none" stroke="var(--sec-dark)" stroke-width="2"/>
  </g>

  <!-- gears icon -->
  <g class="icon icon--gears" fill="var(--erp-icon)">
    <circle cx="512" cy="402" r="20"/>
    <g transform="translate(512 402)">
      <rect x="-5" y="-26" width="10" height="52"/><rect x="-5" y="-26" width="10" height="52" transform="rotate(45)"/>
      <rect x="-5" y="-26" width="10" height="52" transform="rotate(90)"/><rect x="-5" y="-26" width="10" height="52" transform="rotate(135)"/>
    </g>
    <circle cx="512" cy="402" r="9" fill="var(--erp-dark)"/>
    <circle cx="528" cy="434" r="10"/>
    <g transform="translate(528 434)">
      <rect x="-3" y="-14" width="6" height="28"/><rect x="-3" y="-14" width="6" height="28" transform="rotate(60)"/><rect x="-3" y="-14" width="6" height="28" transform="rotate(120)"/>
    </g>
    <circle cx="528" cy="434" r="4" fill="var(--erp-dark)"/>
    <circle cx="489" cy="424" r="4.5"/><circle cx="502" cy="439" r="3.5"/><circle cx="512" cy="450" r="3.5"/>
    <rect x="470" y="428" width="12" height="12" rx="3" transform="rotate(45 476 434)"/>
    <rect x="484" y="443" width="12" height="12" rx="3" transform="rotate(45 490 449)"/>
    <rect x="496" y="455" width="12" height="12" rx="3" transform="rotate(45 502 461)"/>
  </g>

  <!-- gear with circuit icon -->
  <g class="icon icon--circuit-gear">
    <g fill="var(--dig-icon)" transform="translate(684 427)">
      <path d="M0,-28 A28,28 0 1 0 28,0 H16 A16,16 0 1 1 0,-16 Z"/>
      <rect x="-4" y="-33" width="8" height="9" transform="rotate(-60)"/>
      <rect x="-4" y="-33" width="8" height="9" transform="rotate(-110)"/>
      <rect x="-4" y="-33" width="8" height="9" transform="rotate(-160)"/>
      <rect x="-4" y="-33" width="8" height="9" transform="rotate(150)"/>
      <rect x="-4" y="-33" width="8" height="9" transform="rotate(100)"/>
    </g>
    <g stroke="var(--dig-icon)" stroke-width="3" fill="none" stroke-linecap="round">
      <path d="M684,427 L712,399"/><path d="M693,418 L693,402 L700,395"/><path d="M703,408 L716,408 L722,402"/><path d="M698,413 L720,413"/>
    </g>
    <g fill="var(--dig-icon)">
      <circle cx="702" cy="393" r="3.5"/><circle cx="714" cy="397" r="3.5"/><circle cx="724" cy="400" r="3.5"/><circle cx="722" cy="413" r="3.5"/>
    </g>
  </g>

  <circle cx="600" cy="338" r="79" fill="var(--bg)"/>
  <circle cx="600" cy="338" r="66" fill="var(--gold)"/>
</svg>

<section class="segment segment--doc">
  <h2 class="block title title--right" style="left:400px; top:117px; width:172px;">Document<br>Management</h2>
  <div class="block" style="left:111px; top:107px;">
    <p class="summary">Streamline document organization, access, and collaboration with easier file storage and sharing, leading to more efficient workflows.</p>
    <div class="divider divider--doc"></div>
    <ul class="checks">
      <li>Centralized Document Control</li>
      <li>Collaborative Workspace Integration</li>
      <li>Automated Compliance Tracking</li>
      <li>Check 4</li>
    </ul>
  </div>
  <a class="learn-more" href="#" style="left:127px; top:287px;">Learn More</a>
</section>

<section class="segment segment--sec">
  <h2 class="block title" style="left:625px; top:118px;">Security and<br>Compliance</h2>
  <div class="block" style="left:834px; top:107px;">
    <p class="summary">Benefit from tailored cloud solutions, secure data storage, and expert disaster recovery planning for reliable and scalable IT operations.</p>
    <div class="divider divider--sec"></div>
    <ul class="checks">
      <li>Costum Cloud Solutions</li>
      <li>Secure Data Storage</li>
      <li>Expert Disaster Recovery</li>
      <li>Check 4</li>
    </ul>
  </div>
  <a class="learn-more" href="#" style="left:848px; top:287px;">Learn More</a>
</section>

<section class="segment segment--erp">
  <h2 class="block title title--right" style="left:400px; top:511px; width:175px;">Enterprise<br>Resource<br>Planning</h2>
  <div class="block" style="left:111px; top:390px;">
    <p class="summary">Simplify management across finance, sales, and operations, enabling better decision-making and improved productivity.</p>
    <div class="divider divider--erp"></div>
    <ul class="checks">
      <li>Integrated Business Processes</li>
      <li>Enhanced Decision-Making</li>
      <li>Productivity Improvement</li>
      <li>Check 4</li>
    </ul>
  </div>
  <a class="learn-more" href="#" style="left:127px; top:560px;">Learn More</a>
</section>

<section class="segment segment--dig">
  <h2 class="block title" style="left:624px; top:519px;">Digital<br>Transformation</h2>
  <div class="block" style="left:834px; top:375px;">
    <p class="summary">Benefit from tailored cloud solutions, secure data storage, and expert disaster recovery planning for reliable and scalable IT operations.</p>
    <div class="divider divider--dig"></div>
    <ul class="checks">
      <li>Instant searchable Archives with OCR</li>
      <li>Automated Document Classification</li>
      <li>DocShare and Cloud Blob Ready</li>
      <li>Check 4</li>
    </ul>
  </div>
  <a class="learn-more" href="#" style="left:848px; top:560px;">Learn More</a>
</section>

<div class="hub-label">SUPER<br>PRODUCT</div>
</body>
</html>
```